Book cover entitled #LIFTTHEVEIL

Design front book cover (self-self-portait photos included) for my first book entitled -

#LIFTTHEVEIL (may be best to have different shades of colour for lift the veil to stand off you). I'm intentionally choosing a title that is essentially a hashtag.

Subtitle - Unhiding quiet inner burdens today

Concept of cover - left side of my face is shaded with shame and right side is brighter and hopeful. I have also include my logo.

Link for photos
https://www.parcelbin.net/sh/q7rkd2mwx41pzt/QPLm8vRtn3Hs2WkcZdu5BYeLx?dl=0

Target Market(s)

People (or friends & family) suffering with the shame of mental health struggles

Industry/Entity Type

Mental Health

Font styles to use
Other font styles liked:
• Avenir

Colors
3276b5
85acd3
cfdeed

Requirements
Must have
• Relatable, contemporary, authentic & compelling
• Link for photos
• https://www.parcelbin.net/sh/q7rkd2mwx41pzt/QPLm8vRtn3Hs2WkcZdu5BYeLx?dl=0
Nice to have
• Abstract & creative
Should not have
• Cheesy, plastic, pedestrian etc

```html
<!DOCTYPE html>
<html lang="en">
<head>
<meta charset="utf-8">
<title>#LIFTTHEVEIL — Book Cover</title>
<link href="https://fonts.googleapis.com/css2?family=Bebas+Neue&family=Nunito+Sans:wght@600&display=swap" rel="stylesheet">
<style>
  :root {
    --page-bg: #e8e5e1;
    --cover-black: #0b0c0d;
    --title-blue: #3a9ee0;
    --title-blue-deep: #3276b5;
    --subtitle-grey: #b8b8b8;
    --portrait-green: #3f9a55;
    --portrait-teal: #2f7f86;
    --portrait-blue: #3276b5;
    --brand-blue: #85acd3;
  }
  html, body {
    margin: 0;
    width: 1200px;
    height: 900px;
    overflow: hidden;
    background: var(--page-bg);
  }
  .book-cover {
    position: absolute;
    left: 290px;
    top: 20px;
    width: 620px;
    height: 860px;
    background: var(--cover-black);
    overflow: hidden;
  }
  .cover-portrait {
    position: absolute;
    left: 70px;
    top: 50px;
    width: 330px;
    height: 560px;
    background:
      radial-gradient(ellipse 55% 45% at 45% 42%, rgba(63,154,85,0.85), rgba(47,127,134,0.5) 55%, rgba(11,12,13,0) 100%),
      radial-gradient(ellipse 40% 30% at 60% 72%, rgba(50,118,181,0.7), rgba(11,12,13,0) 100%);
  }
  .cover-title {
    position: absolute;
    left: 488px;
    top: 40px;
    margin: 0;
    writing-mode: vertical-rl;
    font-family: "Bebas Neue", sans-serif;
    font-weight: 400;
    font-size: 122px;
    line-height: 1;
    letter-spacing: 5px;
    color: var(--title-blue);
  }
  .cover-title .title-accent { color: var(--title-blue-deep); }
  .cover-subtitle {
    position: absolute;
    left: 426px;
    top: 150px;
    margin: 0;
    writing-mode: vertical-rl;
    font-family: "Bebas Neue", sans-serif;
    font-weight: 400;
    font-size: 45px;
    line-height: 1;
    letter-spacing: 2.5px;
    color: var(--subtitle-grey);
  }
  .author-mark {
    position: absolute;
    left: 0;
    width: 590px;
    top: 748px;
    display: flex;
    justify-content: center;
    align-items: center;
    gap: 10px;
  }
  .author-mark-square {
    width: 22px;
    height: 22px;
    background: var(--brand-blue);
  }
  .author-name {
    font-family: "Nunito Sans", sans-serif;
    font-weight: 600;
    font-size: 20px;
    color: var(--brand-blue);
  }
</style>
</head>
<body>
  <main class="book-cover">
    <div class="cover-portrait" role="img" aria-label="Author self-portrait, half shaded, tinted green and blue, fading into black"></div>
    <h1 class="cover-title"><span class="title-accent">#LIFT</span>THEVEIL</h1>
    <p class="cover-subtitle">UNHIDING QUIET INNER BURDENS TODAY</p>
    <div class="author-mark">
      <span class="author-mark-square"></span>
      <span class="author-name">dan carver</span>
    </div>
  </main>
</body>
</html>
```